CASCADE HAIR STUDIO NEEDS A FLYER MADE

I’m wanting a flyer made up for a letter box drop for my hair salon.
It needs to target Men and Ladies.
I want to list my services we offer.
I also want on the flyer - (Present this flyer to receive
20% off any hair Colour Service)

Also wanting our logo, phone number and address.

I also want to our regular weekly deals on the back.
I will attach a inspirational picture for the flyer.

Industry/Entity Type

Hairdresser

Font styles to use
Serif
Sans Serif
Script

Requirements
Must have
• I want to list my services we offer
- Mens & Ladies Haircuts
- Style Cuts
- Colour Services
- Blowdry & Styling
- Up Styles
- Perming
- Chemical straightening

I also want on the flyer
Present this flyer to receive
20% off any hair Colour Service

Phone: 49537816
Address: Shop 3/214 Kilbride Road, The Larkfield, Mackay QLD 4740

I also want to our weekly deals on the back side.
Mens Day Wednesday
$19.00 Haircuts

Thursday Seniors Day
- Shampoo, Ladies Haircut & Blowdry $35
- Ladies Haircut & Blowdry $30
- Shampoo & Blowdry $27.00
-$5off any colour service
- Perm (includes Trim & Blowdry) $85
- Facial Waxing $10

FRIDAY HAPPY HOUR 3PM – 5PM
- Shampoo, Blow dry & Style $40.00
- Shampoo, Mens Haircut & Style $29.00
(Complimentary beverage on arrival)

BOOK NOW

Follow us on facebook
Nice to have
• Photos of our work (hair) we do.

```html
<!DOCTYPE html>
<html lang="en">
<head>
<meta charset="utf-8">
<title>Cascade Hair Studio – Flyer</title>
<link rel="stylesheet" href="https://fonts.googleapis.com/css2?family=Lato:wght@400;700;900&display=swap">
<style>
  :root {
    --stage: #808080;
    --paper: #ffffff;
    --ink: #111111;
    --panel: #151515;
    --soft: #ececec;
    --rule: #bdbdbd;
    --accent: #f5e614;
    --deal-head: #3d3d3d;
    --deal-foot: #262626;
    --photo-blonde: linear-gradient(160deg, #8a6e55 0%, #d9d2c4 40%, #ebe5d8 60%, #2a2a2a 100%);
    --photo-man: linear-gradient(150deg, #c9c3b8 0%, #8b7462 45%, #2a2a2a 80%);
    --photo-curls: linear-gradient(160deg, #c9b59a 0%, #6b5238 60%, #3b2b1d 100%);
    --photo-salon: linear-gradient(170deg, #d8d2c2 0%, #8d8a6a 50%, #2c3320 100%);
  }
  * { box-sizing: border-box; margin: 0; padding: 0; }
  html, body { width: 1200px; height: 1200px; overflow: hidden; }
  body { background: var(--stage); font-family: "Lato", sans-serif; color: var(--ink); position: relative; }

  .page { position: absolute; top: 242px; width: 512px; height: 663px; background: var(--paper); overflow: hidden; box-shadow: 0 3px 8px rgba(0,0,0,.35); }
  .page--front { left: 74px; }
  .page--back { left: 630px; background: linear-gradient(100deg, #f3f3f3 0%, #ffffff 45%, #eeeeee 100%); }
  .abs { position: absolute; }
  .photo { position: absolute; }

  .brand { position: absolute; text-align: center; font-family: "Lato", sans-serif; font-weight: 400; color: var(--ink); line-height: 1; }
  .brand__name { display: block; font-size: 30px; letter-spacing: 1px; }
  .brand__sub { display: block; font-size: 10px; letter-spacing: 3px; margin-top: 4px; }

  /* front */
  .logo-box { left: 24px; top: 0; width: 285px; height: 171px; border-left: 1px solid var(--rule); border-right: 1px solid var(--rule); border-bottom: 2px solid var(--rule); }
  .page--front .brand { left: 24px; top: 62px; width: 285px; }
  .services-panel { left: 237px; top: 153px; width: 253px; height: 339px; background: var(--panel); }
  .services { left: 324px; top: 211px; color: #fff; }
  .services__title { font-size: 25px; font-weight: 900; letter-spacing: .3px; }
  .services__list { list-style: none; margin-top: 20px; }
  .services__list li { font-size: 13px; line-height: 15.8px; color: #e6e6e6; }
  .services__list li::before { content: "•"; margin-right: 8px; font-size: 10px; }
  .offer { left: 325px; top: 403px; color: #fff; }
  .offer__lead { font-size: 11.5px; }
  .offer__big { font-size: 27px; font-weight: 900; color: var(--accent); line-height: 1.05; }
  .offer__note { font-size: 10px; color: var(--accent); }
  .contact-band { left: 0; top: 584px; width: 512px; height: 79px; background: var(--panel); }
  .contact-soft { left: 24px; top: 477px; width: 283px; height: 186px; background: var(--soft); }
  .contact-soft--ext { left: 237px; top: 584px; width: 70px; height: 79px; background: var(--soft); }
  .phone-line { left: 44px; top: 561px; display: flex; align-items: center; gap: 15px; }
  .phone-line span { font-size: 26px; font-weight: 900; }
  .address-line { left: 44px; top: 598px; display: flex; gap: 16px; align-items: flex-start; }
  .address-line p { font-size: 11.5px; font-weight: 700; line-height: 14.5px; width: 225px; }

  /* back */
  .page--back .brand { left: 0; top: 36px; width: 512px; }
  .frame { left: 24px; top: 126px; width: 284px; height: 424px; border: 1px solid #cfcfcf; }
  .shade { left: 0; top: 529px; width: 512px; height: 56px; background: linear-gradient(90deg, #1f2a36 0%, #3a4450 55%, #c9c9c9 100%); }
  .deals { left: 328px; top: 126px; width: 162px; }
  .deal { height: 52px; margin-bottom: 10px; display: flex; flex-direction: column; text-align: center; }
  .deal__name { flex: 1 1 auto; background: var(--deal-head); color: #fff; font-size: 8px; display: flex; align-items: center; justify-content: center; padding: 0 6px; line-height: 10px; }
  .deal__name b { font-weight: 900; }
  .deal__price { height: 19px; background: var(--deal-foot); color: var(--accent); font-size: 14px; font-weight: 700; line-height: 19px; }
  .deal--day .deal__name { font-size: 13px; font-weight: 900; }
  .deal--day .deal__price { font-size: 11.5px; height: 20px; background: var(--deal-head); border-top: 1px solid #555; }
  .footer { left: 0; top: 584px; width: 512px; height: 79px; background: var(--panel); color: #fff; text-align: center; }
  .footer__phone { margin-top: 14px; display: flex; justify-content: center; align-items: center; gap: 10px; font-size: 24px; font-weight: 900; }
  .footer__addr { margin-top: 4px; display: flex; justify-content: center; align-items: center; gap: 10px; font-size: 12px; }
</style>
</head>
<body>

<section class="page page--front">
  <div class="abs logo-box"></div>
  <div class="brand"><span class="brand__name">CASCADE</span><span class="brand__sub">HAIR STUDIO</span></div>

  <div class="abs services-panel"></div>
  <div class="photo" role="img" aria-label="Side profile of a man with a fresh skin fade haircut" style="left:323px;top:11px;width:166px;height:159px;background:var(--photo-man)"></div>
  <div class="photo" role="img" aria-label="Client with long sleek platinum blonde hair seen from behind" style="left:24px;top:190px;width:283px;height:264px;background:var(--photo-blonde)"></div>

  <div class="abs services">
    <h2 class="services__title">SERVICES</h2>
    <ul class="services__list">
      <li>Mens &amp; Ladies Haircuts</li>
      <li>Style Cuts</li>
      <li>Colour Services</li>
      <li>Blowdry &amp; Styling</li>
      <li>Up Styles</li>
      <li>Perming</li>
      <li>Chemical straightening</li>
    </ul>
  </div>
  <div class="abs offer">
    <p class="offer__lead">Present this flyer to receive</p>
    <p class="offer__big">20% OFF</p>
    <p class="offer__note">Any hair Colour Service</p>
  </div>

  <div class="abs contact-band"></div>
  <div class="abs contact-soft"></div>
  <div class="abs contact-soft--ext"></div>

  <div class="photo" role="img" aria-label="Men's textured haircut from behind" style="left:237px;top:512px;width:70px;height:70px;background:var(--photo-man)"></div>
  <div class="photo" role="img" aria-label="Soft brunette waves" style="left:309px;top:512px;width:90px;height:70px;background:var(--photo-curls)"></div>
  <div class="photo" role="img" aria-label="Balayage curls" style="left:400px;top:512px;width:90px;height:70px;background:var(--photo-curls)"></div>
  <div class="photo" role="img" aria-label="Salon interior with plants" style="left:309px;top:584px;width:181px;height:79px;background:var(--photo-salon)"></div>

  <div class="abs phone-line">
    <svg width="16" height="16" viewBox="0 0 24 24" aria-hidden="true"><path fill="#111" d="M6.6 10.8a15 15 0 0 0 6.6 6.6l2.2-2.2c.3-.3.7-.4 1-.2 1.1.4 2.3.6 3.6.6.6 0 1 .4 1 1V20c0 .6-.4 1-1 1A17 17 0 0 1 3 4c0-.6.4-1 1-1h3.5c.6 0 1 .4 1 1 0 1.3.2 2.5.6 3.6.1.3 0 .7-.2 1z"/></svg>
    <span>49537816</span>
  </div>
  <div class="abs address-line">
    <svg width="16" height="20" viewBox="0 0 24 30" aria-hidden="true"><path fill="#111" d="M12 0a10 10 0 0 0-10 10c0 7.5 10 20 10 20s10-12.5 10-20A10 10 0 0 0 12 0zm0 14a4 4 0 1 1 0-8 4 4 0 0 1 0 8z"/></svg>
    <p>Shop 3/214 Kilbride Road, The Larkfield, Mackay QLD 4740</p>
  </div>
</section>

<section class="page page--back">
  <div class="brand"><span class="brand__name">CASCADE</span><span class="brand__sub">HAIR STUDIO</span></div>
  <div class="abs shade"></div>
  <div class="photo" role="img" aria-label="Man with a classic side-part fade haircut in the salon chair" style="left:0;top:143px;width:289px;height:386px;background:var(--photo-man)"></div>
  <div class="abs frame"></div>

  <div class="abs deals">
    <div class="deal"><div class="deal__name"><span><b>MENS HAIRCUTS</b> DAY WEDNESDAY</span></div><div class="deal__price">$19.00</div></div>
    <div class="deal deal--day"><div class="deal__name">THURSDAY</div><div class="deal__price">Seniors Day</div></div>
    <div class="deal"><div class="deal__name"><span><b>SHAMPOO, LADIES</b> HAIRCUT &amp; BLOWDRY</span></div><div class="deal__price">$35</div></div>
    <div class="deal"><div class="deal__name"><span><b>LADIES</b> HAIRCUT &amp; BLOWDRY</span></div><div class="deal__price">$30</div></div>
    <div class="deal"><div class="deal__name"><span><b>SHAMPOO &amp; BLOWDRY</b></span></div><div class="deal__price">$27.00</div></div>
    <div class="deal"><div class="deal__name"><span><b>PERM (INCLUDES</b> TRIM &amp; BLOWDRY)</span></div><div class="deal__price">$85</div></div>
    <div class="deal"><div class="deal__name"><span><b>FACIAL</b> WAXING</span></div><div class="deal__price">$10</div></div>
  </div>

  <div class="abs footer">
    <div class="footer__phone">
      <svg width="10" height="10" viewBox="0 0 24 24" aria-hidden="true"><path fill="#fff" d="M6.6 10.8a15 15 0 0 0 6.6 6.6l2.2-2.2c.3-.3.7-.4 1-.2 1.1.4 2.3.6 3.6.6.6 0 1 .4 1 1V20c0 .6-.4 1-1 1A17 17 0 0 1 3 4c0-.6.4-1 1-1h3.5c.6 0 1 .4 1 1 0 1.3.2 2.5.6 3.6.1.3 0 .7-.2 1z"/></svg>
      <span>49537816</span>
    </div>
    <div class="footer__addr">
      <svg width="8" height="10" viewBox="0 0 24 30" aria-hidden="true"><path fill="#fff" d="M12 0a10 10 0 0 0-10 10c0 7.5 10 20 10 20s10-12.5 10-20A10 10 0 0 0 12 0zm0 14a4 4 0 1 1 0-8 4 4 0 0 1 0 8z"/></svg>
      <span>Shop 3/214 Kilbride Road, The Larkfield, Mackay QLD 4740</span>
    </div>
  </div>
</section>

</body>
</html>
```